Poster to inspire rural women around Australia!

We need a poster for our upcoming annual women's events in 2017. The poster will be used for every event this year (needs to be editable in Adobe suite of products) as a template sent to our event hosts around regional Australia. Our group will be hosting 3 events When the Doubters fall quiet / Can crafty neighbours lift each other? / Living with loss. We would like the design to be able to work across these 3 topics and to be clean, honest and use imagery which is meaningful for our target audience. Examples of previous posters attached.

Target Market(s)

'The Wanderers'; 30 - 60 year old women who live in regional Australia and have been removed from their normal conversations channels because of family (young or old).

Industry/Entity Type

Events

Font styles to use
Sans Serif

Colors
eda3c7
eaf2ce
f9d9e8
cadf82

Requirements
Must have
• A4 size poster
• Editable using Adobe products
• Organisation name - The Marrowbank Circle
• Event name, date, venue, time, booking details and price
Nice to have
• Our colours (themarrowbankcircle.com.au) green & pink
• tag line 'connecting women with conversation'

```html
<!DOCTYPE html>
<html lang="en">
<head>
<meta charset="utf-8">
<title>The Marrowbank Circle — Poster</title>
<link rel="stylesheet" href="https://fonts.googleapis.com/css2?family=Cinzel:wght@400&family=Arimo:wght@400&display=swap">
<style>
  :root {
    --white-glow: #fff8fc;
    --pink-light: #f9d9e8;
    --pink-mid: #f4b2df;
    --pink-deep: #ec96d2;
    --green-haze: #cadf82;
    --green-field: #a3c77c;
    --green-deep: #9cc377;
    --tagline: #de2f8c;
    --title: #1d1a1b;
    --label: #2b2b2b;
  }
  html, body {
    margin: 0;
    padding: 0;
    width: 848px;
    height: 1200px;
    overflow: hidden;
    background: #ffffff;
  }
  .poster {
    position: relative;
    width: 848px;
    height: 1200px;
    overflow: hidden;
    font-family: "Arimo", Arial, sans-serif;
  }
  .poster__photo {
    position: absolute;
    inset: 0;
    background:
      radial-gradient(ellipse 170px 150px at 420px 575px, rgba(255,255,255,1) 0%, rgba(255,255,255,0.7) 45%, rgba(255,255,255,0) 100%),
      radial-gradient(ellipse 520px 230px at 424px 110px, rgba(255,255,255,0.98) 0%, rgba(255,250,253,0.75) 50%, rgba(255,250,253,0) 100%),
      radial-gradient(ellipse 160px 260px at 60px 560px, rgba(190,200,140,0.35) 0%, rgba(190,200,140,0) 100%),
      radial-gradient(ellipse 150px 240px at 790px 620px, rgba(190,200,140,0.3) 0%, rgba(190,200,140,0) 100%),
      linear-gradient(180deg,
        var(--pink-light) 0%,
        var(--pink-mid) 26%,
        var(--pink-deep) 44%,
        #f0a8da 60%,
        #ecb6dc 68%,
        #d7c2b6 74%,
        #bfd08f 79%,
        var(--green-field) 84%,
        var(--green-deep) 100%);
  }
  .poster__title {
    position: absolute;
    top: 42px;
    left: 0;
    width: 100%;
    margin: 0;
    text-align: center;
    font-family: "Cinzel", Georgia, serif;
    font-weight: 400;
    font-size: 56px;
    line-height: 66px;
    letter-spacing: 1px;
    text-transform: uppercase;
    color: var(--title);
  }
  .poster__tagline {
    position: absolute;
    top: 660px;
    left: 0;
    width: 100%;
    margin: 0;
    text-align: center;
    font-weight: 400;
    font-size: 79px;
    line-height: 78px;
    letter-spacing: -0.5px;
    color: var(--tagline);
  }
  .event-details {
    position: absolute;
    top: 1062px;
    left: 94px;
    right: 94px;
    display: flex;
    justify-content: space-between;
    font-size: 27px;
    line-height: 40px;
    color: var(--label);
  }
  .event-details__column {
    display: flex;
    flex-direction: column;
    width: 140px;
  }
</style>
</head>
<body>
  <main class="poster">
    <div class="poster__photo" role="img" aria-label="Pink-tinted photograph of two women in hats seen from behind, arms raised, running through a sunlit green field"></div>

    <h1 class="poster__title">The Marrowbank<br>Circle</h1>

    <p class="poster__tagline">connecting women<br>with conversation</p>

    <section class="event-details">
      <div class="event-details__column">
        <span class="event-details__label">Date:</span>
        <span class="event-details__label">Venue:</span>
      </div>
      <div class="event-details__column">
        <span class="event-details__label">Time:</span>
        <span class="event-details__label">Price:</span>
      </div>
    </section>
  </main>
</body>
</html>
```